we are a college and require a design of a printable graduation certificate

our courses range from certicate III to Diploma

We would a high quality design, similar to a unveristy degree, so its meaning full to the students and looks great on the wall

our college website is: www.marlowinstitute.example.au

Industry/Entity Type

College

Requirements
Must have
• security feature like water mark or stamp

```html
<!DOCTYPE html>
<html lang="en">
<head>
<meta charset="utf-8">
<title>Marlow Institute – Certificate of Graduation</title>
<link href="https://fonts.googleapis.com/css2?family=UnifrakturMaguntia&display=swap" rel="stylesheet">
<style>
  :root {
    --frame-blue: #0a32ff;
    --frame-cyan: #33f0ff;
    --paper: #ffffff;
    --ink: #0b0b0b;
    --seal-blue: #1f48e8;
    --seal-cyan: #3de3ff;
  }
  * { margin: 0; padding: 0; box-sizing: border-box; }
  html, body { width: 852px; height: 1200px; overflow: hidden; background: var(--paper); }
  .certificate {
    position: relative;
    width: 852px;
    height: 1200px;
    background: var(--frame-blue);
    padding: 18px;
    font-family: "UnifrakturMaguntia", "Old English Text MT", serif;
    color: var(--ink);
  }
  .frame-gap { width: 100%; height: 100%; background: var(--paper); padding: 4px; }
  .frame-band { width: 100%; height: 100%; background: var(--frame-cyan); padding: 12px; }
  .sheet { position: relative; width: 100%; height: 100%; background: var(--paper); }
  .text-line { position: absolute; left: 0; right: 0; text-align: center; line-height: 1.2; }

  .brand { position: absolute; left: 0; right: 0; top: 52px; text-align: center; }
  .brand-dot { display: block; margin: 0 auto 14px; width: 118px; height: 118px; border-radius: 50%; background: var(--frame-blue); }
  .brand-name { font-size: 30px; color: var(--ink); }

  .title { top: 268px; font-size: 49px; }
  .intro { top: 350px; font-size: 19px; }
  .conferred { top: 436px; font-size: 19px; }
  .recipient { top: 508px; font-size: 41px; }
  .requirements { top: 594px; font-size: 19px; }
  .degree { top: 696px; font-size: 43px; line-height: 1.15; }
  .rights { top: 846px; font-size: 20px; line-height: 1.4; }

  .signatory { position: absolute; top: 1006px; font-size: 13px; }
  .signatory--chair { left: 110px; }
  .signatory--president { right: 108px; }
  .seal { position: absolute; left: 50%; top: 946px; transform: translateX(-50%); }
</style>
</head>
<body>
  <main class="certificate">
    <div class="frame-gap">
      <div class="frame-band">
        <section class="sheet">
          <header class="brand">
            <span class="brand-dot"></span>
            <span class="brand-name">Marlow Institute</span>
          </header>

          <h1 class="text-line title">Certificate of Graduation</h1>
          <p class="text-line intro">In recognition of successful completion of the requisite<br>course of study</p>
          <p class="text-line conferred">The College of Regents has conferred upon</p>
          <p class="text-line recipient">Any name Here</p>
          <p class="text-line requirements">in recognition of the satisfactory fulfillment of prescribed<br>requirements for the degree of</p>
          <p class="text-line degree">Business &amp; Management<br>course</p>
          <p class="text-line rights">with the rights, honors, &amp; privileges thereunto appertaining<br>Dated this first of January two thousand &amp; thirteen</p>

          <p class="signatory signatory--chair">Chairman of the Board</p>
          <svg class="seal" width="176" height="176" viewBox="0 0 176 176" role="img" aria-label="Institute security stamp">
            <circle cx="88" cy="88" r="86" fill="var(--seal-cyan)"/>
            <circle cx="88" cy="88" r="70" fill="var(--seal-blue)"/>
            <circle cx="88" cy="88" r="44" fill="var(--paper)"/>
          </svg>
          <p class="signatory signatory--president">President of College</p>
        </section>
      </div>
    </div>
  </main>
</body>
</html>
```